Modern Lawfirm Business Card Design

We're looking for a business card to incorporate the newly created logo we had made.

Ideally looking for a law firm business card demonstrating, modern, minimalist, strong/bold design.

I'm open to any design honestly, but nothing "flashy".

Target Market(s)

Immigration law, family immigration, humanitarian, general legal

Industry/Entity Type

Law Firm

Contact Information for Business Card

Please use dummy information, name, street address, city, state, phone number, email, website.

Font styles to use
Serif
Sans Serif

Requirements
Must have
• Please use dummy information, name, street address, city, state, phone number, email, website.

```html
<!DOCTYPE html>
<html lang="en">
<head>
<meta charset="utf-8">
<title>Varela Immigration Law – Business Card</title>
<link href="https://fonts.googleapis.com/css2?family=Roboto:wght@300;400;500&display=swap" rel="stylesheet">
<style>
  :root {
    --page-bg: #ebe7e7;
    --card-white: #f7f7f6;
    --card-blue: #2b67a1;
    --brand-blue: #1f5ba6;
    --ink: #1d1d1f;
    --ink-soft: #333338;
    --rule: #3a3a3d;
    --white: #ffffff;
  }
  * { box-sizing: border-box; margin: 0; padding: 0; }
  html, body {
    width: 974px; height: 1200px; overflow: hidden;
    background: var(--page-bg);
    font-family: "Roboto", Arial, sans-serif;
  }
  .canvas { position: relative; width: 974px; height: 1200px; }

  .card {
    position: absolute; left: 167px;
    width: 640px; height: 365px;
  }
  .card-front { top: 175px; background: var(--card-white); }
  .card-back  { top: 632px; background: var(--card-blue); }

  .person { position: absolute; left: 45px; top: 40px; }
  .person-name { font-size: 23px; font-weight: 500; color: var(--ink); letter-spacing: 0.2px; }
  .person-title { font-size: 14px; font-weight: 400; color: var(--brand-blue); margin-top: 4px; }

  .brand {
    position: absolute; display: flex; align-items: center; gap: 8px;
    font-weight: 500; letter-spacing: 2px;
  }
  .brand-mark { display: block; }
  .card-front .brand { right: 40px; top: 42px; font-size: 30px; color: var(--brand-blue); }
  .card-front .brand-mark { width: 14px; height: 14px; background: var(--brand-blue); }
  .card-back .brand {
    left: 50%; top: 50%; transform: translate(-50%, -50%);
    font-size: 48px; color: var(--white);
  }
  .card-back .brand-mark { width: 22px; height: 22px; background: var(--white); }

  .divider {
    position: absolute; left: 45px; right: 40px; top: 261px;
    height: 1px; background: var(--rule);
  }

  .contact, .office {
    position: absolute; top: 269px;
    font-size: 15px; font-weight: 300; line-height: 23px; color: var(--ink-soft);
  }
  .contact { left: 45px; }
  .contact-label { font-weight: 500; color: var(--brand-blue); margin-right: 3px; }
  .office { right: 40px; text-align: right; }
  .office-name { font-weight: 500; color: var(--ink); }
</style>
</head>
<body>
<main class="canvas">
  <section class="card card-front">
    <div class="person">
      <h1 class="person-name">JOHN SMITH</h1>
      <p class="person-title">Managing Director</p>
    </div>
    <div class="brand"><span class="brand-mark"></span>VARELA</div>
    <div class="divider"></div>
    <ul class="contact" style="list-style:none">
      <li><span class="contact-label">P</span>000-111-22-333</li>
      <li><span class="contact-label">E</span>johnsmith@varelalaw.com</li>
      <li><span class="contact-label">W</span>www.varelalaw.com</li>
    </ul>
    <address class="office" style="font-style:normal">
      <div class="office-name">Varela Immigration Law</div>
      <div>7788 Street Name Street Name</div>
      <div>City Name</div>
    </address>
  </section>

  <section class="card card-back">
    <div class="brand"><span class="brand-mark"></span>VARELA</div>
  </section>
</main>
</body>
</html>
```